Business Cards for Tech Company - uBrightowl

We would like new modern business cards designed for our company. Attached are some examples of other business cards we like. <br/><br/>Info we need is: <br/>First Name, Last Name<br/>Address<br/>Store Phone<br/>Cell Phone<br/>Email Address<br/>Text Logo <br/>And Other Logo<br/>

Industry/Entity Type

Technology Equipment

Contact Information for Business Card

Please use these details as example:

Dale Morrow
Technology Specialist
Direct 555.617.2094
Phone 555-730-8186

dale.morrow@ubrightowl.example

2971 Willet Lane
Alderbrook, QX 00427

Font styles to use
Sans Serif
Other font styles liked:
• Anything easy to read and modern

Colors

Designer to choose colors to be used in the design.

Requirements
Must have
• Both Logos
• Signature as name
• Use the text logo and use the shark logo but do not use the full shark logo. Have it where it is zoomed in and is expanding out of the card.
Nice to have
• Keep it clean and modern
• We like blue, white, and black/grays.
Should not have
• Random icons for phone and address.

```html
<!DOCTYPE html>
<html lang="en">
<head>
<meta charset="utf-8">
<title>uBrightowl Business Card</title>
<link rel="stylesheet" href="https://fonts.googleapis.com/css2?family=Source+Sans+3:wght@300;400;600&family=Allura&display=swap">
<style>
  :root {
    --black: #000000;
    --charcoal: #2d2d2d;
    --glow: #3a3a3a;
    --white: #ffffff;
    --row-1: #f4f4f4;
    --row-2: #ebebeb;
    --row-3: #dadada;
    --blue-1: #0287d5;
    --blue-2: #0074c6;
    --blue-3: #005fae;
    --blue-fold: #1d4fa0;
    --ink: #1e1e1e;
    --logo-grey: #7b7d80;
  }
  html, body {
    margin: 0;
    padding: 0;
    width: 1000px;
    height: 1200px;
    overflow: hidden;
    background: var(--white);
  }
  .canvas {
    position: relative;
    width: 1000px;
    height: 1200px;
    font-family: "Source Sans 3", sans-serif;
  }
  /* Front face */
  .card-front {
    position: absolute;
    left: 0; top: 0;
    width: 1000px; height: 600px;
    background: radial-gradient(ellipse 480px 330px at 50% 48%, var(--glow) 0%, #151617 55%, var(--black) 100%);
  }
  .wordmark {
    position: absolute;
    display: flex;
    align-items: center;
    gap: 14px;
    font-weight: 600;
    font-size: 58px;
    letter-spacing: -1px;
    color: var(--logo-grey);
    white-space: nowrap;
  }
  .wordmark .mark-dot {
    width: 34px; height: 34px;
    border-radius: 50%;
    background: var(--blue-2);
  }
  .card-front .wordmark {
    left: 50%; top: 300px;
    transform: translate(-50%, -50%);
  }
  /* Back face */
  .card-back {
    position: absolute;
    left: 0; top: 600px;
    width: 1000px; height: 600px;
    background: var(--white);
  }
  .identity-panel {
    position: absolute;
    left: 0; top: 0;
    width: 508px; height: 600px;
    background: var(--charcoal);
  }
  .identity-panel .wordmark {
    left: 270px; top: 262px;
    transform: translate(-50%, -50%);
  }
  .signature {
    position: absolute;
    left: 270px; top: 375px;
    transform: translate(-50%, -50%);
    font-family: "Allura", cursive;
    font-size: 54px;
    color: var(--white);
    white-space: nowrap;
  }
  .job-title {
    position: absolute;
    left: 270px; top: 437px;
    transform: translate(-50%, -50%);
    font-size: 21px;
    font-weight: 400;
    letter-spacing: 5.5px;
    color: var(--white);
    white-space: nowrap;
  }
  .title-rule {
    position: absolute;
    left: 228px; top: 456px;
    width: 85px; height: 3px;
    background: var(--blue-1);
  }
  .contact-ribbon {
    position: absolute;
    left: 477px; top: 111px;
  }
  .contact-rows {
    position: absolute;
    left: 590px; top: 140px;
    width: 410px;
  }
  .contact-row {
    display: flex;
    flex-direction: column;
    justify-content: center;
    padding-left: 37px;
    box-sizing: border-box;
    color: var(--ink);
    font-weight: 300;
    white-space: nowrap;
  }
  .contact-row.phones { height: 107px; background: var(--row-1); font-size: 34px; line-height: 44px; }
  .contact-row.email { height: 106px; background: var(--row-2); font-size: 23px; font-weight: 400; }
  .contact-row.address { height: 105px; background: var(--row-3); font-size: 24px; font-weight: 400; line-height: 31px; }
</style>
</head>
<body>
<div class="canvas">
  <section class="card-front">
    <div class="wordmark"><span class="mark-dot"></span>uBrightowl</div>
  </section>

  <section class="card-back">
    <div class="identity-panel">
      <div class="wordmark"><span class="mark-dot"></span>uBrightowl</div>
      <div class="signature">Dale Morrow</div>
      <div class="job-title">TECHNOLOGY SPECIALIST</div>
      <div class="title-rule"></div>
    </div>

    <svg class="contact-ribbon" width="113" height="374" viewBox="0 0 113 374" aria-hidden="true">
      <polygon points="0,29 31,0 31,29" fill="var(--blue-fold)"/>
      <polygon points="0,346 31,346 31,374" fill="var(--blue-fold)"/>
      <rect x="0" y="29" width="113" height="107" fill="var(--blue-1)"/>
      <rect x="0" y="136" width="113" height="106" fill="var(--blue-2)"/>
      <rect x="0" y="242" width="113" height="104" fill="var(--blue-3)"/>
      <!-- phone -->
      <g fill="none" stroke="var(--white)" stroke-width="3.5">
        <rect x="44" y="58" width="25" height="48" rx="3"/>
        <line x1="44" y1="66" x2="69" y2="66"/>
        <line x1="44" y1="96" x2="69" y2="96"/>
      </g>
      <circle cx="56.5" cy="101" r="2" fill="var(--white)"/>
      <!-- envelope -->
      <rect x="33" y="171" width="47" height="34" fill="var(--white)"/>
      <polyline points="33,171 56.5,191 80,171" fill="none" stroke="var(--blue-2)" stroke-width="3.5"/>
      <line x1="33" y1="205" x2="50" y2="188" stroke="var(--blue-2)" stroke-width="3"/>
      <line x1="63" y1="188" x2="80" y2="205" stroke="var(--blue-2)" stroke-width="3"/>
      <!-- pin -->
      <path d="M56.5 268 a20 20 0 0 1 20 20 c0 15 -20 34 -20 34 c0 0 -20 -19 -20 -34 a20 20 0 0 1 20 -20z" fill="var(--white)"/>
      <circle cx="56.5" cy="288" r="7" fill="var(--blue-3)"/>
    </svg>

    <div class="contact-rows">
      <div class="contact-row phones"><span>555-617-2094</span><span>555-730-8186</span></div>
      <div class="contact-row email">dale.morrow@ubrightowl.example</div>
      <div class="contact-row address"><span>2971 Willet Lane Alderbrook,</span><span>QX 00427</span></div>
    </div>
  </section>
</div>
</body>
</html>
```